Website re-design

I have opened a new frozen yogurt store that will eventually expand into fresh juices and smoothies. I have built a website myself and need to have something that better reflects the brand direction I want to go in.

here is the existing site:
http://www.plumhollowa.com

here is our facebook page, which will be changed to reflect the new web design:
https://www.facebook.com/PlumHollowa

Our look and feel direction will be
Fresh, natural/rustic homemade, quirky, fun

Once I have a new website I will re-launch all of our print collateral to fit with this central part of our communication strategy.

Our brand Vision is listed below
At Plum Hollowa our vision is to create a healthy smile in everyday by constantly delivering deep emotional connections with delicious products in a cool environment.
Updates

Reason: Hi Designers, great work so far. I have extended the deadline as I would like the website to be a one page site with pages that follow on from each other. I will respond to you all shortly.

Hi All, thanks so much for your great work so far.  My existing site uses the Orbel theme, but if you think a different theme would better fit the fresh, rustic and fun approach then please submit designs using this theme.  I am happy to go with a completely different look to what I have now.  

I guess when people come to the site I want it to create a appetite that makes them smile.  Some lines for us are:

Deliciously skinny
Putting a smile in your appetite
Super Plum Hollowa

HI Designers I have posted more photos to the brief and an update to the brief to show you what our store looks like.  We use a lot of old window shutters and blackboards to communicate with customers.  The feeling is very warm and rustic.  I would ideally love if this same look and feel carried across to the website.  I am open to any new ideas you may have.

Target Market(s)

My primary target market is females aged 15 - 25 and secondary is females aged 30 to 55. Every single person who tries our product talks about how diferent the flavours are and what we offer. I need to be able to share this with new potential customers who come across our website.

Industry/Entity Type

Communication

Requirements
Must have
• Fresh images of fruit and yogurt and must take a quirky fun approach to all aspects of the site. Buttons and even headers can all have a quirky approach. The name of plum hollowa is supposed to reflect the yogurt is low fat, but also be a bit cheeky.
Nice to have
• Our store design uses a lots of blackboards and shutters on the roof. It would be nice if our website reflected this rustic homemade warm feel. I would love for there to be a continuation of this feel to the site. I have uploaded some images of the store to the brief to show you what type and look and feel we have in the store

```html
<!DOCTYPE html>
<html lang="en">
<head>
<meta charset="utf-8">
<title>Plum Hollowa – Frozen Yogurt</title>
<link href="https://fonts.googleapis.com/css2?family=Lato:wght@400;700&family=Dancing+Script:wght@500&display=swap" rel="stylesheet">
<style>
  :root {
    --page-bg: #f6f2e2;
    --panel-bg: #ffffff;
    --text: #3d3a36;
    --brown: #5a3410;
    --brown-dark: #4a2a0c;
    --green-light: #a6dc24;
    --green: #86c30f;
    --sky: #5fb8d6;
    --rose: #ee6b6b;
    --navy: #3f5c9c;
    --amber: #f2bd3c;
    --crimson: #cb2330;
  }
  * { box-sizing: border-box; margin: 0; padding: 0; }
  html, body {
    width: 1200px; height: 821px; overflow: hidden;
    background: var(--page-bg);
    font-family: "Lato", sans-serif;
    color: var(--text);
  }
  .panel {
    position: absolute; left: 144px; top: 0;
    width: 929px; height: 821px;
    background: var(--panel-bg);
    box-shadow: 0 0 4px rgba(0,0,0,0.12);
  }
  .product {
    position: absolute; top: 88px; width: 251px; text-align: center;
  }
  .product__photo {
    width: 251px; height: 186px; border-radius: 16px;
  }
  .product__photo--kiwi { background: radial-gradient(circle at 50% 45%, #f4eee6 0%, #d9d5cc 55%, #6f6a55 100%); }
  .product__photo--nuts { background: radial-gradient(circle at 50% 55%, #e9e2d5 0%, #8c5a3a 55%, #4a3a30 100%); }
  .product__photo--berry { background: radial-gradient(circle at 50% 50%, #f4f1ee 0%, #c52a2e 55%, #3c3a36 100%); }
  .product__text {
    margin: 14px -6px 0; font-size: 16.5px; line-height: 17px;
  }
  .btn {
    display: inline-block; margin-top: 12px;
    width: 131px; height: 45px; line-height: 45px; border-radius: 22px;
    background: linear-gradient(var(--green-light), var(--green));
    color: #2f3a12; font-size: 16.5px; text-decoration: none;
  }
  .info {
    position: absolute; top: 432px;
  }
  .info__title {
    font-family: "Dancing Script", cursive; font-weight: 500;
    font-size: 29px; color: var(--brown-dark); margin-left: 103px;
  }
  .info__icon {
    position: absolute; left: 0; top: 44px;
    width: 90px; height: 90px; border-radius: 50%;
    display: flex; align-items: center; justify-content: center;
    box-shadow: 0 4px 3px rgba(0,0,0,0.25), inset 0 0 0 3px #fff;
  }
  .info__icon--green { background: var(--green); }
  .info__icon--brown { background: var(--brown); }
  .info__body { margin: 12px 0 0 103px; width: 320px; }
  .info__body p { font-size: 16.5px; line-height: 17px; margin-bottom: 16px; }
  .info__link {
    display: inline-block; margin-top: 2px; font-size: 14.5px; color: var(--brown-dark);
    text-decoration: underline; margin-left: 2px;
  }
  .site-nav {
    position: absolute; top: 675px; left: 0; width: 100%;
    display: flex; justify-content: center; align-items: center; gap: 15px;
    font-family: "Dancing Script", cursive; font-size: 23px; color: var(--brown-dark);
    list-style: none; padding-left: 4px;
  }
  .site-nav .dot { width: 6px; height: 6px; border-radius: 50%; background: var(--brown-dark); }
  .social {
    position: absolute; top: 730px; left: 0; width: 100%;
    display: flex; justify-content: center; gap: 14px;
  }
  .social span { width: 41px; height: 41px; border-radius: 50%; }
  .copyright {
    position: absolute; top: 782px; left: 0; width: 100%;
    text-align: center; font-size: 14.5px; color: var(--brown-dark);
  }
</style>
</head>
<body>
<main class="panel">
  <section class="product" style="left:25px">
    <div class="product__photo product__photo--kiwi" role="img" aria-label="Cup of frozen yogurt topped with kiwi"></div>
    <p class="product__text">Cyatsvitae eryas nemerat niptalas<br>ecaerat iades metrase kaystas<br>miausases.</p>
    <a class="btn" href="#">Know More</a>
  </section>
  <section class="product" style="left:340px">
    <div class="product__photo product__photo--nuts" role="img" aria-label="Cup of frozen yogurt with nuts and berries"></div>
    <p class="product__text">Cyatsvitae eryas nemerat niptalas<br>ecaerat iades metrase kaystas<br>miausases.</p>
    <a class="btn" href="#">Know More</a>
  </section>
  <section class="product" style="left:656px">
    <div class="product__photo product__photo--berry" role="img" aria-label="Cup of frozen yogurt topped with strawberries"></div>
    <p class="product__text">Cyatsvitae eryas nemerat niptalas<br>ecaerat iades metrase kaystas<br>miausases.</p>
    <a class="btn" href="#">Know More</a>
  </section>

  <section class="info" style="left:44px">
    <h2 class="info__title">Nutritional Info</h2>
    <div class="info__icon info__icon--green">
      <svg width="34" height="30" viewBox="0 0 34 30"><path d="M17 29 C6 20 1 15 1 9 A8 8 0 0 1 17 6 A8 8 0 0 1 33 9 C33 15 28 20 17 29Z" fill="#fff"/></svg>
    </div>
    <div class="info__body">
      <p>Cyatsvitae eryas nemerat niptalas ecaerat<br>iades metrase kaystas miausases.</p>
      <p>Cyatsvitae eryas nemerat niptalas ecaerat<br>iades metrase kaystas miausases.</p>
      <a class="info__link" href="#">Read More</a>
    </div>
  </section>

  <section class="info" style="left:495px">
    <h2 class="info__title" style="margin-left:128px">Testimonial</h2>
    <div class="info__icon info__icon--brown">
      <svg width="44" height="44" viewBox="-22 -22 44 44">
        <g fill="#fff">
          <ellipse cx="0" cy="-11" rx="6" ry="10"/>
          <ellipse cx="0" cy="-11" rx="6" ry="10" transform="rotate(72)"/>
          <ellipse cx="0" cy="-11" rx="6" ry="10" transform="rotate(144)"/>
          <ellipse cx="0" cy="-11" rx="6" ry="10" transform="rotate(216)"/>
          <ellipse cx="0" cy="-11" rx="6" ry="10" transform="rotate(288)"/>
        </g>
        <circle r="4" fill="#5a3410"/>
      </svg>
    </div>
    <div class="info__body" style="margin-left:105px">
      <p>Cyatsvitae eryas nemerat niptalas ecaerat<br>iades metrase kaystas miausases.</p>
      <p>Cyatsvitae eryas nemerat niptalas ecaerat<br>iades metrase kaystas miausases.</p>
      <a class="info__link" href="#">More Testimonial</a>
    </div>
  </section>

  <nav>
    <ul class="site-nav">
      <li>Home</li><li class="dot"></li>
      <li>About</li><li class="dot"></li>
      <li>Products</li><li class="dot"></li>
      <li>Career</li><li class="dot"></li>
      <li>Franchise</li><li class="dot"></li>
      <li>Contact Us</li>
    </ul>
  </nav>

  <div class="social">
    <span style="background:var(--sky)" role="img" aria-label="Social link"></span>
    <span style="background:var(--rose)" role="img" aria-label="Social link"></span>
    <span style="background:var(--navy)" role="img" aria-label="Social link"></span>
    <span style="background:var(--amber)" role="img" aria-label="Feed link"></span>
    <span style="background:var(--crimson)" role="img" aria-label="Social link"></span>
  </div>

  <p class="copyright">©2013, All Rights Reserved,Plum Hollowa</p>
</main>
</body>
</html>
```